Business Card Design Project

We need business cards for our new business, Veltrano Skyworks. We specialize in aerial videography and photography via drone. Currently we are mainly focusing on real estate videography but will branch into other markets and may even host training classes for flying drones.
Cards should include:
Name
Phone Number
Email Address
Web address
We will need to customize for more than one person and would like those fields to be editable
eps file logos are uploaded now, thanks!
Target Market(s)
Real Estate Agents, hotels, rental agencies and people who have recently purchase drones
Industry/Entity Type
Videography

```html
<!DOCTYPE html>
<html lang="en">
<head>
<meta charset="utf-8">
<title>Veltrano Skyworks – Business Card</title>
<link href="https://fonts.googleapis.com/css2?family=Open+Sans:wght@400;600&display=swap" rel="stylesheet">
<style>
  :root {
    --backdrop: #d4d4d4;
    --card-black: #111214;
    --card-black-soft: #23252a;
    --card-white: #ffffff;
    --accent: #f7a21b;
    --accent-deep: #e8860d;
    --text-light: #f2f2f2;
    --text-muted: #c9c9c9;
    --logo-dark: #2a2a2a;
    --logo-silver: #d8d8d8;
  }
  * { box-sizing: border-box; margin: 0; padding: 0; }
  html, body { width: 1200px; height: 900px; overflow: hidden; }
  body {
    background: var(--backdrop);
    font-family: "Open Sans", Arial, sans-serif;
    display: flex;
    align-items: center;
    justify-content: center;
    gap: 60px;
  }
  .card {
    width: 525px;
    height: 300px;
    border-radius: 22px;
    overflow: hidden;
    position: relative;
    box-shadow: 0 14px 30px rgba(0,0,0,0.25);
  }

  /* Front */
  .card-front { background: var(--card-black); display: flex; flex-direction: column; }
  .front-header {
    height: 128px;
    background: var(--card-white);
    display: flex;
    align-items: center;
    padding-left: 22px;
    gap: 12px;
  }
  .brand-mark {
    width: 44px; height: 44px;
    background: var(--accent);
    flex: none;
  }
  .brand-name {
    font-weight: 600;
    font-size: 30px;
    color: var(--logo-dark);
    letter-spacing: 0.5px;
  }
  .accent-band {
    height: 13px;
    background: linear-gradient(90deg, var(--accent-deep), var(--accent));
  }
  .front-body {
    flex: 1;
    position: relative;
    background: radial-gradient(ellipse at 70% 40%, var(--card-black-soft), var(--card-black) 70%);
    padding: 14px 22px;
    color: var(--text-light);
  }
  .person-name { font-size: 17px; font-weight: 600; color: var(--accent); line-height: 1.1; }
  .person-title { font-size: 10px; color: var(--text-light); margin-bottom: 22px; }
  .contact-list { list-style: none; }
  .contact-item {
    display: flex; align-items: center; gap: 6px;
    font-size: 13px; line-height: 19px;
  }
  .contact-item svg { width: 12px; height: 12px; fill: var(--accent); flex: none; }
  .drone-photo {
    position: absolute;
    right: 20px; top: 22px;
    width: 200px; height: 110px;
    border-radius: 50%;
    background: radial-gradient(ellipse at center, #3a3a3a 0%, #222 45%, rgba(30,30,30,0) 72%);
  }

  /* Back */
  .card-back {
    background: radial-gradient(ellipse at 50% 45%, var(--card-black-soft), var(--card-black) 75%);
    display: flex; flex-direction: column; align-items: center; justify-content: center;
    gap: 18px;
  }
  .back-mark { width: 78px; height: 78px; background: var(--accent); }
  .back-name {
    font-weight: 600;
    font-size: 34px;
    color: var(--logo-silver);
    letter-spacing: 1px;
  }
</style>
</head>
<body>

  <section class="card card-front">
    <header class="front-header">
      <span class="brand-mark"></span>
      <span class="brand-name">Veltrano Skyworks</span>
    </header>
    <div class="accent-band"></div>
    <div class="front-body">
      <p class="person-name">Dana Merritt</p>
      <p class="person-title">Manager</p>
      <ul class="contact-list">
        <li class="contact-item">
          <svg viewBox="0 0 24 24"><path d="M6.6 10.8a15.1 15.1 0 0 0 6.6 6.6l2.2-2.2a1 1 0 0 1 1-.25 11.4 11.4 0 0 0 3.6.57 1 1 0 0 1 1 1V20a1 1 0 0 1-1 1A17 17 0 0 1 3 4a1 1 0 0 1 1-1h3.5a1 1 0 0 1 1 1c0 1.25.2 2.45.57 3.57a1 1 0 0 1-.25 1z"/></svg>
          154-555-0192
        </li>
        <li class="contact-item">
          <svg viewBox="0 0 24 24"><path d="M12 2a10 10 0 1 0 0 20 10 10 0 0 0 0-20zm6.9 6h-3a15.7 15.7 0 0 0-1.4-3.6A8 8 0 0 1 18.9 8zM12 4c.8 1.2 1.5 2.5 1.9 4h-3.8c.4-1.5 1.1-2.8 1.9-4zM4.3 14a8 8 0 0 1 0-4h3.4a16 16 0 0 0 0 4zm.8 2h3a15.7 15.7 0 0 0 1.4 3.6A8 8 0 0 1 5.1 16zm3-8h-3a8 8 0 0 1 4.4-3.6C8.9 5.5 8.4 6.7 8.1 8zM12 20c-.8-1.2-1.5-2.5-1.9-4h3.8c-.4 1.5-1.1 2.8-1.9 4zm2.3-6H9.7a14.6 14.6 0 0 1 0-4h4.6a14.6 14.6 0 0 1 0 4zm.2 5.6a15.7 15.7 0 0 0 1.4-3.6h3a8 8 0 0 1-4.4 3.6zm1.8-5.6a16 16 0 0 0 0-4h3.4a8 8 0 0 1 0 4z"/></svg>
          www.veltranosky.com
        </li>
        <li class="contact-item">
          <svg viewBox="0 0 24 24"><path d="M3 5h18a1 1 0 0 1 1 1v12a1 1 0 0 1-1 1H3a1 1 0 0 1-1-1V6a1 1 0 0 1 1-1zm1 2.2V17h16V7.2l-8 5.3z"/></svg>
          hello@veltranosky.com
        </li>
        <li class="contact-item">
          <svg viewBox="0 0 24 24"><path d="M12 3l10 9h-3v9h-5v-6h-4v6H5v-9H2z"/></svg>
          48 Orchard Ln. Milford, NJ. 08848
        </li>
      </ul>
      <div class="drone-photo" role="img" aria-label="Photo of a camera drone with orange arms"></div>
    </div>
  </section>

  <section class="card card-back">
    <span class="back-mark"></span>
    <span class="back-name">Veltrano Skyworks</span>
  </section>

</body>
</html>
```